Vowsbridge-Officiants.com Rack Card Design, Double-Sided. See Attachments.

Please use the attached graphics and the contents of www.vowsbridge-officiants.com to create a rack card that has the same look, feel and colors as the website, business card and existing logos. Your design must be consistent with how the business cards and website currently look.

Target Market(s)

weddings. Visit www.vowsbridge-officiants.com for content and design ideas.

Requirements
Must have
• Same info as business card plus content from the website.

```html
<!DOCTYPE html>
<html lang="en">
<head>
<meta charset="utf-8">
<title>Vowsbridge-Officiants.com Rack Card</title>
<link rel="stylesheet" href="https://fonts.googleapis.com/css2?family=Bodoni+Moda:ital,wght@1,400&family=Questrial&display=swap">
<style>
  :root {
    --peach: #fddcae;
    --peach-dot: #fbd39c;
    --paper: #ffffff;
    --ink: #1f1f1f;
    --backdrop: #eeeeee;
    --rose-light: #f3c9c2;
    --rose-mid: #e2a49a;
    --leaf: #3d5a44;
  }
  * { box-sizing: border-box; margin: 0; padding: 0; }
  html, body {
    width: 1047px;
    height: 1200px;
    overflow: hidden;
    background: var(--backdrop);
  }
  .canvas {
    position: relative;
    width: 1047px;
    height: 1200px;
    font-family: "Questrial", sans-serif;
    color: var(--ink);
  }
  .card {
    position: absolute;
    top: 105px;
    width: 440px;
    height: 990px;
    overflow: hidden;
  }
  .card--front { left: 60px; background: var(--peach); }
  .card--back { left: 547px; background: var(--paper); }

  /* Front */
  .front-top {
    position: absolute;
    inset: 0 0 auto 0;
    height: 320px;
    background: var(--paper);
  }
  .brand-name {
    position: absolute;
    top: 78px;
    width: 100%;
    text-align: center;
    font-size: 25px;
    letter-spacing: 0.5px;
    color: var(--ink);
  }
  .hero-photo {
    position: absolute;
    left: 81px;
    top: 180px;
    width: 278px;
    height: 278px;
    border-radius: 50%;
    border: 5px solid var(--paper);
    background: radial-gradient(circle at 40% 40%, var(--rose-light) 0%, var(--rose-mid) 55%, var(--leaf) 100%);
  }
  .headline {
    position: absolute;
    top: 510px;
    width: 100%;
    text-align: center;
    font-family: "Bodoni Moda", serif;
    font-style: italic;
    font-weight: 400;
    font-size: 36px;
    line-height: 46px;
  }
  .rule {
    position: absolute;
    left: 62px;
    right: 62px;
    border-top: 1.5px dashed var(--ink);
  }
  .rule--upper { top: 677px; }
  .rule--lower { top: 820px; }
  .pitch {
    position: absolute;
    top: 712px;
    left: 70px;
    right: 70px;
    text-align: center;
    font-size: 17px;
    line-height: 27px;
  }
  .contact {
    position: absolute;
    top: 862px;
    width: 100%;
    text-align: center;
    font-size: 17px;
    line-height: 24px;
    list-style: none;
  }

  /* Back */
  .back-top {
    position: absolute;
    inset: 0 0 auto 0;
    height: 321px;
    background: var(--peach);
    border-bottom: 1.5px dashed var(--ink);
  }
  .section-title {
    position: absolute;
    top: 135px;
    width: 100%;
    text-align: center;
    font-family: "Bodoni Moda", serif;
    font-style: italic;
    font-weight: 400;
    font-size: 35px;
  }
  .service-list {
    position: absolute;
    top: 379px;
    width: 100%;
    list-style: none;
    text-align: center;
    font-size: 16.5px;
  }
  .service-list li {
    height: 49px;
    line-height: 24px;
  }
  .service-list li::before {
    content: "";
    display: inline-block;
    width: 8px;
    height: 8px;
    border-radius: 50%;
    background: var(--peach-dot);
    margin-right: 12px;
    vertical-align: 2px;
  }
  .floral-art {
    position: absolute;
    left: 90px;
    top: 670px;
    width: 260px;
    height: 300px;
    border-radius: 45% 55% 50% 50%;
    background: radial-gradient(ellipse at 50% 45%, #f6ddd6 0%, #f2c4b4 40%, rgba(242,196,180,0.35) 70%, rgba(255,255,255,0) 100%);
  }
</style>
</head>
<body>
<main class="canvas">
  <section class="card card--front">
    <div class="front-top"></div>
    <p class="brand-name">Vowsbridge-Officiants.com</p>
    <div class="hero-photo" role="img" aria-label="Bouquet of pale pink roses with green leaves"></div>
    <h1 class="headline">Professional<br>Network of Related<br>Services</h1>
    <div class="rule rule--upper"></div>
    <p class="pitch">Reduce Your Stress and Save Time. Let's Use My Network of Professional Providers.</p>
    <div class="rule rule--lower"></div>
    <ul class="contact">
      <li>www.vowsbridge-officiants.com</li>
      <li>hello@Vowsbridge-Officiants.com</li>
      <li>(860) 555-0147</li>
    </ul>
  </section>

  <section class="card card--back">
    <div class="back-top"></div>
    <h2 class="section-title">Event Services</h2>
    <ul class="service-list">
      <li>Floral Arrangement Coordination</li>
      <li>Professional Photographer Coordination</li>
      <li>Hair &amp; Makeup Coordination</li>
      <li>From Here to There to There</li>
      <li>Coordination of Small Receptions</li>
      <li>You Can Event Sail Away!</li>
    </ul>
    <div class="floral-art" role="img" aria-label="Watercolour-style pale pink rose with small coral and green sprigs"></div>
  </section>
</main>
</body>
</html>
```